Boutique Soy Candle Company Needs a Label Design

We need a label design for a boutique soy candle company based in Kelby, South Australia.
We sell high quality, hand poured soy wax candles, melts and reed diffusers.
We are based in a coastal town and would like the label to reflect our rustic, beachy, retro but luxurious feel. I've attached the design we've been using and like the idea but want to have something more professional. The picture of the Venner Spire is something that we would like to be included somehow - it's like our town symbol - a 'lighthouse' of sorts. It was quite stylised on my original design but we are open to different interpretations.
We like the idea of a 'Kraft' brown paper sort of label but are not set on it. We also love the fluro pink look.

```html
<!DOCTYPE html>
<html lang="en">
<head>
<meta charset="utf-8">
<title>Gleam Soy Candle Co – Label Options</title>
<link href="https://fonts.googleapis.com/css2?family=Archivo+Black&family=Josefin+Sans:wght@400&display=swap" rel="stylesheet">
<style>
  :root {
    --paper: #ffffff;
    --navy: #1b3340;
    --cream: #ffffff;
    --fluoro: #e8157a;
    --fluoro-soft: #f3a6c9;
  }
  * { box-sizing: border-box; margin: 0; padding: 0; }
  html, body {
    width: 1200px; height: 379px; overflow: hidden;
    background: var(--paper);
  }
  .canvas { position: relative; width: 1200px; height: 379px; }
  .label {
    position: absolute; top: 16px;
    background: var(--navy);
    padding: 12px;
  }
  .label--compact { left: 104px; width: 437px; height: 362px; }
  .label--bold { left: 672px; width: 432px; height: 362px; }
  .label__frame {
    width: 100%; height: 100%;
    border: 3px solid var(--cream);
    display: flex; flex-direction: column; align-items: center;
    color: var(--cream);
    font-family: "Josefin Sans", sans-serif;
  }
  .label__company {
    margin-top: 36px;
    font-size: 25px; line-height: 1; letter-spacing: 1px;
  }
  .label__brand {
    margin-top: 20px;
    font-family: "Archivo Black", sans-serif;
    font-weight: 400;
    color: var(--fluoro);
    font-size: 56px; line-height: 1;
    letter-spacing: 12px; text-indent: 12px;
  }
  .label--bold .label__brand {
    margin-top: 14px;
    font-size: 64px; letter-spacing: 18px; text-indent: 18px;
  }
  .label__made {
    margin-top: 16px;
    display: flex; align-items: center; gap: 16px;
  }
  .label--bold .label__made { margin-top: 12px; }
  .label__word {
    font-size: 21px; line-height: 1; letter-spacing: 1px;
    border-top: 2px dotted var(--cream);
    border-bottom: 2px dotted var(--cream);
    padding: 8px 4px 6px;
  }
  .label__spire {
    width: 30px; height: 54px;
    background: linear-gradient(var(--fluoro-soft), var(--fluoro));
  }
  .label__place {
    margin-top: 28px;
    font-size: 19px; letter-spacing: 1px;
    transform: rotate(4deg);
  }
</style>
</head>
<body>
<main class="canvas">
  <section class="label label--compact">
    <div class="label__frame">
      <p class="label__company">SOY CANDLE Co</p>
      <h1 class="label__brand">GLEAM</h1>
      <div class="label__made">
        <span class="label__word">HAND</span>
        <div class="label__spire" role="img" aria-label="Stylised striped Venner Spire, the town symbol"></div>
        <span class="label__word">MADE</span>
      </div>
      <p class="label__place">KELBY SOUTH AUSTRALIA</p>
    </div>
  </section>
  <section class="label label--bold">
    <div class="label__frame">
      <p class="label__company">SOY CANDLE Co</p>
      <h1 class="label__brand">GLEAM</h1>
      <div class="label__made">
        <span class="label__word">HAND</span>
        <div class="label__spire" role="img" aria-label="Stylised striped Venner Spire, the town symbol"></div>
        <span class="label__word">MADE</span>
      </div>
      <p class="label__place">KELBY SOUTH AUSTRALIA</p>
    </div>
  </section>
</main>
</body>
</html>
```